Membership Sales Page Web Design

We need a website designed to showcase the benefits of joining our online community of technology procurement professionals.

Our community has been around for a while and it's time for a refresh. Included in the brief is Verson 1.0 of the site. You can see the current version of the site @ brindlehub.com.

As part of the refresh, we've acquired a new primary domain name (brindle.com) and will be rolling out both a free and paid subscription model.

Because of this, there should be a strong call to sign (join now) infused within the site.

We would like to see site designs that are clean, flat and minimalistic in nature. Our membership colors are royal blue, grey, and white.

The final design should communicate networking and professional growth.

I'd be particularly interestedin seeing some flat website designs with a strong call to action. Here are some great examples for inspiration:

https://pivotlyst.com/
https://marrowkit.io/

Target Market(s)

vantage 400 companies

Number of Pages Required

1 page

Font styles to use
Sans Serif

Colors
0293ce
3276b5
ffffff

Requirements
Must have
• clean, minimalistic, fee
strong call to action
showcase our different membership levels
highlight the benefits of membership
Nice to have
• n/a
Should not have
• n/a

```html
<!DOCTYPE html>
<html lang="en">
<head>
<meta charset="utf-8">
<title>Brindle — Membership</title>
<link href="https://fonts.googleapis.com/css2?family=Montserrat:ital,wght@0,400;0,500;0,600;0,700;1,400&display=swap" rel="stylesheet">
<style>
:root{
  --blue:#0293ce;
  --royal:#3276b5;
  --white:#ffffff;
  --ink:#1e1e1e;
  --text:#555a60;
  --muted:#9a9ea3;
  --grey-bg:#f2f2f2;
  --line:#e3e3e3;
  --navy-a:#27265d;
  --navy-b:#4a4e8f;
  --green:#3bb54a;
}
*{margin:0;padding:0;box-sizing:border-box}
html,body{width:1200px;height:3557px;overflow:hidden}
body{position:relative;font-family:'Montserrat',sans-serif;color:var(--ink);background:var(--white)}
.abs{position:absolute}
.btn{position:absolute;display:flex;align-items:center;justify-content:center;background:var(--blue);color:var(--white);font-weight:600;font-size:16px}
.btn-outline{background:transparent;border:2px solid var(--blue)}
.section-title{position:absolute;left:0;width:1200px;text-align:center;font-weight:600;font-size:16px;letter-spacing:.2px}
.section-title span{position:relative}
.section-title span::after{content:"";position:absolute;left:50%;bottom:-6px;width:48px;height:2px;margin-left:-24px;background:var(--blue)}

/* header */
.site-header{position:absolute;left:0;top:0;width:1200px;height:87px;background:var(--white)}
.search{left:73px;top:6px;width:134px;height:23px;background:#ececec;border-radius:2px;font-size:12px;font-style:italic;color:#777;display:flex;align-items:center;padding-left:8px;gap:6px}
.brand{left:0;width:1200px;top:4px;text-align:center}
.brand-name{font-weight:700;font-size:28px;color:var(--royal);letter-spacing:1px;line-height:30px}
.brand-sub{font-size:6px;color:var(--royal);letter-spacing:.3px}
.contact{left:895px;top:4px;font-size:12px;display:flex;align-items:center;gap:5px}
.social{left:1046px;top:5px;display:flex;gap:9px}
.social i{display:block;width:13px;height:13px;border-radius:50%;background:#b9bcc0}
.nav a{position:absolute;top:56px;font-size:14px;font-weight:500;color:var(--ink);text-decoration:none}
.nav .current::after{content:"";position:absolute;left:22px;right:22px;bottom:-6px;height:2px;background:var(--blue)}
.nav-join{left:947px;top:54px;width:107px;height:24px;font-size:14px}
.login{left:1068px;top:56px;font-size:14px;font-weight:500;display:flex;align-items:center;gap:4px}

/* hero */
.hero{position:absolute;left:0;top:87px;width:1200px;height:465px;background:linear-gradient(180deg,#4a4338 0%,#3a362f 45%,#2f2c28 100%)}
.hero::after{content:"";position:absolute;inset:0;background:rgba(0,0,0,.3)}
.hero-copy{position:absolute;left:0;top:212px;width:1200px;text-align:center;color:var(--white);z-index:1}
.hero-title{font-size:28px;font-weight:700;letter-spacing:.2px}
.hero-sub{font-size:16px;font-weight:500;margin-top:2px;color:#e6e6e6}
.hero .btn{z-index:1;top:313px;width:195px;height:48px}
.scroll-cue{left:581px;top:533px;width:38px;height:38px;border-radius:50%;background:var(--white);box-shadow:0 2px 6px rgba(0,0,0,.15);display:flex;align-items:center;justify-content:center}

/* about */
.about{position:absolute;left:0;top:639px;width:1200px;height:593px;background:var(--grey-bg)}
.about-lead{position:absolute;left:0;top:74px;width:1200px;text-align:center;font-size:14px;font-style:italic;color:var(--text)}
.card{position:absolute;top:118px;width:249px;height:331px;background:var(--white);box-shadow:0 2px 6px rgba(0,0,0,.12);text-align:center;padding:28px 14px 0}
.card::before{content:"";position:absolute;left:0;top:0;right:0;height:4px;background:linear-gradient(90deg,var(--blue),var(--royal))}
.card h3{font-size:15px;font-weight:600;position:relative;display:inline-block;margin-bottom:32px}
.card h3::after{content:"";position:absolute;left:50%;bottom:-7px;width:30px;height:2px;margin-left:-15px;background:var(--blue)}
.card p{font-size:12px;line-height:23.5px;color:var(--text)}
.card p b{color:var(--ink);font-weight:600}

/* member band */
.member{position:absolute;left:0;top:1305px;width:1200px;height:450px;background:linear-gradient(120deg,#2b2c2e 0%,#1e2226 50%,#2a2d31 100%);color:var(--white)}
.member::after{content:"";position:absolute;inset:0;background:rgba(0,0,0,.25)}
.member > *{z-index:1}
.member .section-title{top:56px;color:var(--white)}
.member-copy{position:absolute;left:150px;top:124px;width:900px;text-align:center;font-size:14px;font-weight:600;line-height:24px}
.benefit{position:absolute;font-size:14px;font-weight:600;display:flex;align-items:center;gap:8px}
.member .btn{left:474px;top:356px;width:254px;height:47px}

/* pricing */
.pricing{position:absolute;left:0;top:1880px;width:1200px;height:654px;background:var(--grey-bg)}
.pricing .section-title{top:22px}
.billing{position:absolute;left:0;top:66px;width:1200px;display:flex;justify-content:center;gap:32px;font-size:13px;font-weight:500}
.billing span{display:flex;align-items:center;gap:4px}
.billing .save{color:var(--green)}
.radio{width:10px;height:10px;border-radius:50%;border:1px solid #666;display:inline-flex;align-items:center;justify-content:center}
.radio.on::after{content:"";width:4px;height:4px;border-radius:50%;background:var(--blue)}
.plan-table{position:absolute;left:144px;top:100px;width:910px;display:grid;grid-template-columns:227px 227px 228px 228px;grid-template-rows:64px 66px 66px 85px repeat(6,33px) 38px;background:var(--white)}
.plan-table > div{border-right:1px solid var(--line);border-bottom:1px solid var(--line);display:flex;align-items:center;justify-content:center;font-size:12px}
.plan-table > div:nth-child(4n){border-right:none}
.intro{grid-row:1 / span 3;background:#f5f5f5;flex-direction:column;align-items:flex-start !important;justify-content:center;padding-left:30px}
.intro h2{font-size:25px;font-weight:600;color:var(--blue);line-height:32px}
.intro p{font-size:11px;color:#b3b3b3;line-height:17px;margin-top:10px;width:140px}
.plan-name{background:#f5f5f5;font-size:14px !important;font-weight:500;color:#555}
.plan-name.top{color:var(--ink);font-weight:600;background:var(--white)}
.price{background:#f5f5f5;color:var(--blue);font-size:22px !important;font-weight:500}
.price sup{font-size:9px;margin-left:1px}
.price.top{background:var(--white)}
.signup{background:#f5f5f5}
.signup.top{background:var(--white)}
.signup span{display:flex;align-items:center;justify-content:center;width:122px;height:30px;background:var(--blue);color:var(--white);font-weight:600;font-size:12px}
.feat-head{justify-content:flex-start !important;align-items:flex-start !important;padding:22px 0 0 35px;color:#c2c2c2;font-size:11px !important}
.plan-desc{text-align:center;color:var(--text);font-size:11px !important;line-height:17px;padding:0 40px}
.plan-desc.top{color:var(--ink)}
.feat{justify-content:flex-start !important;padding-left:35px;font-size:11px !important;font-weight:500}
.plan-highlight{position:absolute;left:826px;top:1976px;width:228px;height:521px;box-shadow:0 3px 10px rgba(0,0,0,.18);pointer-events:none}
.ribbon{position:absolute;left:986px;top:1980px;width:68px;height:68px;overflow:hidden}
.ribbon span{position:absolute;left:6px;top:16px;width:100px;transform:rotate(45deg);background:var(--green);color:var(--white);font-size:8px;font-weight:700;text-align:center;padding:3px 0}

/* testimonial */
.testimonial{position:absolute;left:0;top:2681px;width:1200px;height:475px;background:linear-gradient(90deg,var(--navy-a) 0%,#343675 55%,var(--navy-b) 100%)}
.quote-mark{left:346px;top:58px}
.quote-text{position:absolute;left:80px;top:143px;width:602px;text-align:center;color:var(--white);font-size:27px;font-weight:600;line-height:40px}
.quote-author{position:absolute;left:80px;top:311px;width:602px;text-align:center;color:#a7a9cf;font-size:16px}
.testimonial .btn{left:284px;top:368px;width:195px;height:49px}
.portrait{position:absolute;left:884px;top:2596px;width:316px;height:560px;background:linear-gradient(180deg,#d9d6d2 0%,#6c6f88 45%,#2f3254 100%);border-radius:120px 120px 0 0}

/* footer */
.site-footer{position:absolute;left:0;top:3248px;width:1200px;height:309px;background:#f4f4f4}
.footer-brand{left:73px;top:54px;font-size:28px;font-weight:700;color:var(--royal);letter-spacing:1px}
.footer-about{position:absolute;left:73px;top:110px;width:360px;font-size:11.5px;line-height:19.5px;color:var(--text)}
.footer-col{position:absolute;top:76px;font-size:12px}
.footer-col h4{font-size:12px;font-weight:500;margin-bottom:19px}
.footer-col a{display:block;color:var(--text);text-decoration:none;margin-bottom:13px}
.to-top{left:1126px;top:113px;width:34px;height:34px;border-radius:50%;background:var(--white);box-shadow:0 2px 6px rgba(0,0,0,.15);display:flex;align-items:center;justify-content:center}
.footer-rule{left:73px;top:218px;width:1028px;height:1px;background:#dcdcdc}
.copyright{left:73px;top:260px;font-size:9.5px;color:var(--text)}
.legal{left:1019px;top:261px;font-size:9.5px;color:var(--text);display:flex;gap:13px}
</style>
</head>
<body>

<header class="site-header">
  <div class="abs search">
    <svg width="11" height="11" viewBox="0 0 12 12"><circle cx="7" cy="5" r="4" fill="none" stroke="#555" stroke-width="1.4"/><path d="M4 8L1 11" stroke="#555" stroke-width="1.4"/></svg>search
  </div>
  <div class="abs brand">
    <div class="brand-sub">Network of</div>
    <div class="brand-name">BRINDLE</div>
    <div class="brand-sub">Sourcing &amp; Vendor Leaders</div>
  </div>
  <div class="abs contact">
    <svg width="14" height="14" viewBox="0 0 24 24"><path fill="#0293ce" d="M6.6 10.8a15.1 15.1 0 0 0 6.6 6.6l2.2-2.2a1 1 0 0 1 1-.25 11.4 11.4 0 0 0 3.6.57 1 1 0 0 1 1 1V20a1 1 0 0 1-1 1A17 17 0 0 1 3 4a1 1 0 0 1 1-1h3.5a1 1 0 0 1 1 1c0 1.25.2 2.45.57 3.57a1 1 0 0 1-.25 1z"/></svg>
    Call 555-014-2290
  </div>
  <div class="abs social"><i></i><i></i><i></i><i></i></div>
  <nav class="nav">
    <a style="left:73px;font-weight:600">Home</a>
    <a class="current" style="left:156px">Join BRINDLE</a>
    <a style="left:289px">BRINDLE Store</a>
    <a style="left:431px">Certification BPL/BPX</a>
    <a style="left:644px">Upcoming Events</a>
    <a style="left:808px">Career Center</a>
  </nav>
  <a class="btn nav-join">Join Now</a>
  <div class="abs login">
    <svg width="12" height="12" viewBox="0 0 12 12"><circle cx="6" cy="3.5" r="2.8" fill="#0293ce"/><path d="M1 12a5 5 0 0 1 10 0z" fill="#0293ce"/></svg>Log in
  </div>
</header>

<section class="hero" role="img" aria-label="Photo of a group of young professionals working together around laptops">
  <div class="hero-copy">
    <h1 class="hero-title">INDUSTRY SPECIFIC CERTIFICATION PROGRAMS.</h1>
    <p class="hero-sub">Invest in your Profession, Your Workforce, Your Future, Yourself</p>
  </div>
  <a class="btn" style="left:400px">Join Now</a>
  <a class="btn btn-outline" style="left:605px">Learn More</a>
</section>
<div class="abs scroll-cue">
  <svg width="14" height="9" viewBox="0 0 14 9"><path d="M1 1l6 6 6-6" fill="none" stroke="#0293ce" stroke-width="2"/></svg>
</div>

<section class="about">
  <h2 class="section-title" style="top:32px"><span>WHO WE ARE?</span></h2>
  <p class="about-lead">Learn from your peers, get answers to your daily questions, thrive in this ever-changing procurement industry.</p>
  <article class="card" style="left:73px">
    <h3>What is BRINDLE?</h3>
    <p>BRINDLE is the only association serving the specialized needs of the technology acquistion professional the person responsible for negotiating and managing contracts and services.</p>
  </article>
  <article class="card" style="left:341px">
    <h3>What is its mission?</h3>
    <p>The BRINDLE mission is to promote and support excellence and professionalism among technology procurement professionals. Brindle works diligently to increase the effectiveness, the image and the impact of these professionals as they serve their organizations and constituents.</p>
  </article>
  <article class="card" style="left:610px">
    <h3>Why should i join?</h3>
    <p>As a member, you will learn what kind of deals others are doing, share information and experiences, obtain information about vendor ploys and pracrices, stay informed on best and worst deals, keep up with legislaive and regulatory issues affecting your job, and <b>much more.</b></p>
  </article>
  <article class="card" style="left:878px">
    <h3>Who is BRINDLE?</h3>
    <p>BRINDLE members come from a variety of skill levels and disciplines from all sectors of the economy, including procurement, finance, legal, information technology and contract management. Their organization vary from single- practitioner shops to large, highly specialized departments.</p>
  </article>
  <a class="btn" style="left:503px;top:496px;width:194px;height:47px">Join Now</a>
</section>

<section class="member" role="img" aria-label="Overhead photo of a team's desk with laptops, notebooks and coffee">
  <h2 class="section-title"><span>BECOME A MEMBER TODAY</span></h2>
  <p class="member-copy">If you're the person responsible for negotiating and managing contracts with vendors of technology products and services, BRINDLE membership is for you. It will enhance your performance and facilitate your professional growth while you network with others to advance the art and science of technology procurement.</p>
  <div class="benefit" style="left:73px;top:238px"><svg width="15" height="15" viewBox="0 0 16 16"><circle cx="8" cy="8" r="7" fill="none" stroke="#0293ce" stroke-width="1.3"/><path d="M4.5 8.2l2.4 2.3 4.6-5" fill="none" stroke="#0293ce" stroke-width="1.5"/></svg>Work Smart</div>
  <div class="benefit" style="left:269px;top:238px"><svg width="15" height="15" viewBox="0 0 16 16"><circle cx="8" cy="8" r="7" fill="none" stroke="#0293ce" stroke-width="1.3"/><path d="M4.5 8.2l2.4 2.3 4.6-5" fill="none" stroke="#0293ce" stroke-width="1.5"/></svg>Gain valuable skills</div>
  <div class="benefit" style="left:486px;top:239px"><svg width="15" height="15" viewBox="0 0 16 16"><circle cx="8" cy="8" r="7" fill="none" stroke="#0293ce" stroke-width="1.3"/><path d="M4.5 8.2l2.4 2.3 4.6-5" fill="none" stroke="#0293ce" stroke-width="1.5"/></svg>Counter vendor ploys</div>
  <div class="benefit" style="left:809px;top:237px"><svg width="15" height="15" viewBox="0 0 16 16"><circle cx="8" cy="8" r="7" fill="none" stroke="#0293ce" stroke-width="1.3"/><path d="M4.5 8.2l2.4 2.3 4.6-5" fill="none" stroke="#0293ce" stroke-width="1.5"/></svg>Interact with your peers about vendors</div>
  <div class="benefit" style="left:73px;top:285px"><svg width="15" height="15" viewBox="0 0 16 16"><circle cx="8" cy="8" r="7" fill="none" stroke="#0293ce" stroke-width="1.3"/><path d="M4.5 8.2l2.4 2.3 4.6-5" fill="none" stroke="#0293ce" stroke-width="1.5"/></svg>Do Better Deals</div>
  <div class="benefit" style="left:269px;top:285px"><svg width="15" height="15" viewBox="0 0 16 16"><circle cx="8" cy="8" r="7" fill="none" stroke="#0293ce" stroke-width="1.3"/><path d="M4.5 8.2l2.4 2.3 4.6-5" fill="none" stroke="#0293ce" stroke-width="1.5"/></svg>Advance your career</div>
  <div class="benefit" style="left:486px;top:286px"><svg width="15" height="15" viewBox="0 0 16 16"><circle cx="8" cy="8" r="7" fill="none" stroke="#0293ce" stroke-width="1.3"/><path d="M4.5 8.2l2.4 2.3 4.6-5" fill="none" stroke="#0293ce" stroke-width="1.5"/></svg>Save time, money and aggravation</div>
  <div class="benefit" style="left:809px;top:284px"><svg width="15" height="15" viewBox="0 0 16 16"><circle cx="8" cy="8" r="7" fill="none" stroke="#0293ce" stroke-width="1.3"/><path d="M4.5 8.2l2.4 2.3 4.6-5" fill="none" stroke="#0293ce" stroke-width="1.5"/></svg>Share working solutions to real situations</div>
  <a class="btn">Become a Member</a>
  <svg class="abs" style="left:818px;top:348px" width="52" height="40" viewBox="0 0 52 40"><path d="M48 2C46 18 34 26 16 28" fill="none" stroke="#0293ce" stroke-width="6" stroke-linecap="round"/><path d="M20 16L6 29l16 9z" fill="#0293ce"/></svg>
</section>

<section class="pricing">
  <h2 class="section-title"><span>CHOOSE THE PLAN THAT'S RIGHT FOR YOU</span></h2>
  <div class="billing">
    <span><i class="radio on"></i>Annually <em class="save" style="font-style:normal">(save 20%)</em></span>
    <span><i class="radio"></i>Monthly</span>
  </div>
  <div class="plan-table">
    <div class="intro"><h2>Pricing<br>Table</h2><p>Lorem ipsum dolor sit amet, consectetur adipisicing elit,aliqua.</p></div>
    <div class="plan-name">Free</div>
    <div class="plan-name">Standart</div>
    <div class="plan-name top">Plus</div>
    <div class="price">$0<sup>.00</sup></div>
    <div class="price">$49<sup>.99</sup></div>
    <div class="price top">$99<sup>.99</sup></div>
    <div class="signup"><span>Sign Up</span></div>
    <div class="signup"><span>Sign Up</span></div>
    <div class="signup top"><span>Sign Up</span></div>
    <div class="feat-head">Feature</div>
    <div class="plan-desc">Lorem ipsum dolor sit amet, consectetur adipisicing elit,aliqua.</div>
    <div class="plan-desc">Lorem ipsum dolor sit amet, consectetur adipisicing elit,aliqua.</div>
    <div class="plan-desc top">Lorem ipsum dolor sit amet, consectetur adipisicing elit,aliqua.</div>

    <div class="feat">Feature One</div>
    <div><svg width="12" height="10" viewBox="0 0 12 10"><path d="M1 5l3.5 3.5L11 1.5" fill="none" stroke="#3276b5" stroke-width="1.8"/></svg></div>
    <div><svg width="12" height="10" viewBox="0 0 12 10"><path d="M1 5l3.5 3.5L11 1.5" fill="none" stroke="#3276b5" stroke-width="1.8"/></svg></div>
    <div><svg width="12" height="10" viewBox="0 0 12 10"><path d="M1 5l3.5 3.5L11 1.5" fill="none" stroke="#3276b5" stroke-width="1.8"/></svg></div>

    <div class="feat">Feature Two</div>
    <div><svg width="12" height="10" viewBox="0 0 12 10"><path d="M1 5l3.5 3.5L11 1.5" fill="none" stroke="#3276b5" stroke-width="1.8"/></svg></div>
    <div><svg width="12" height="10" viewBox="0 0 12 10"><path d="M1 5l3.5 3.5L11 1.5" fill="none" stroke="#3276b5" stroke-width="1.8"/></svg></div>
    <div><svg width="12" height="10" viewBox="0 0 12 10"><path d="M1 5l3.5 3.5L11 1.5" fill="none" stroke="#3276b5" stroke-width="1.8"/></svg></div>

    <div class="feat">Feature Three</div>
    <div></div>
    <div></div>
    <div><svg width="12" height="10" viewBox="0 0 12 10"><path d="M1 5l3.5 3.5L11 1.5" fill="none" stroke="#3276b5" stroke-width="1.8"/></svg></div>

    <div class="feat">Feature Four</div>
    <div></div>
    <div><svg width="12" height="10" viewBox="0 0 12 10"><path d="M1 5l3.5 3.5L11 1.5" fill="none" stroke="#3276b5" stroke-width="1.8"/></svg></div>
    <div><svg width="12" height="10" viewBox="0 0 12 10"><path d="M1 5l3.5 3.5L11 1.5" fill="none" stroke="#3276b5" stroke-width="1.8"/></svg></div>

    <div class="feat">Feature Five</div>
    <div></div>
    <div></div>
    <div><svg width="12" height="10" viewBox="0 0 12 10"><path d="M1 5l3.5 3.5L11 1.5" fill="none" stroke="#3276b5" stroke-width="1.8"/></svg></div>

    <div class="feat">Feature Six</div>
    <div></div>
    <div></div>
    <div><svg width="12" height="10" viewBox="0 0 12 10"><path d="M1 5l3.5 3.5L11 1.5" fill="none" stroke="#3276b5" stroke-width="1.8"/></svg></div>

    <div></div><div></div><div></div><div></div>
  </div>
</section>
<div class="plan-highlight"></div>
<div class="ribbon"><span>Most Popular</span></div>

<section class="testimonial">
  <svg class="abs quote-mark" width="62" height="50" viewBox="0 0 62 50"><path fill="#0293ce" d="M4 50V30C4 14 12 4 26 0l3 6C21 10 17 16 17 24h11v26zM37 50V30C37 14 45 4 59 0l3 6c-8 4-12 10-12 18h11v26z"/></svg>
  <blockquote class="quote-text">Lorem ipsum dolor sit amet, consectetur adipiscing elit, sed do eiusmod tempor incididunt ut labore.</blockquote>
  <p class="quote-author">Dana Whitfield &nbsp; Founder @Lorem ipsum</p>
  <a class="btn">Join Now</a>
</section>
<div class="portrait" role="img" aria-label="Portrait photo of a smiling businesswoman holding documents"></div>

<footer class="site-footer">
  <div class="abs footer-brand">BRINDLE</div>
  <p class="footer-about">BRINDLE is the only association serving the specialized needs of the technology acquisition professional - the person responsible for negotiating and managing contracts with suppliers of technology products and services.</p>
  <div class="footer-col" style="left:538px"><h4>Website</h4><a>Home</a><a>Pricing</a></div>
  <div class="footer-col" style="left:740px"><h4>About Us</h4><a>What we do</a><a>FAQs</a></div>
  <div class="footer-col" style="left:990px"><h4>Acces</h4><a>Login</a><a>Start for free</a></div>
  <div class="abs to-top"><svg width="14" height="9" viewBox="0 0 14 9"><path d="M1 8l6-6 6 6" fill="none" stroke="#0293ce" stroke-width="2"/></svg></div>
  <div class="abs footer-rule"></div>
  <p class="abs copyright">© 2020 BRINDLE. All rights reserved</p>
  <p class="abs legal"><span>Terms</span><span>Privacy</span></p>
</footer>

</body>
</html>
```